NEW STORE PROMOTION FLYER

We need a flyer design for a new lingerie store based in Double Bay.
The people living in Double Bay are most wealthy suburb in Sydney. Our customers are aged at 30+ to 70.
We are offering 'up to 30% off' on selected products.
we recommend using our theme colour: light pink, red, white
the address is:
shop 5/214 Marlow Crest Rd, NSW 2173
contact number: 02 8415 3907
We need key information:
1. we want to let neighborhood know that we open a new store.
2. we offer 'up to 30% off' Christmas Sale
3. Please use our theme colour: light pink, red, white
4. Please add the address map on flyer (you may design again if you need )
5.open hour:
Mon - Fri 10:00am - 5:30pm
Sat - Sun 10:00am - 5:30pm
thank you
aged 30+ to 70; they are relatively wealthy.
Store

```html
<!DOCTYPE html>
<html lang="en">
<head>
<meta charset="utf-8">
<title>Lunelle Lingerie – New Store Christmas Sale</title>
<link href="https://fonts.googleapis.com/css2?family=Baloo+2:wght@700;800&family=Oswald:wght@700&family=Roboto:wght@400;700&family=Tinos&display=swap" rel="stylesheet">
<style>
  :root {
    --red: #e5112d;
    --magenta: #e4007c;
    --pink-light: #fde8f2;
    --pink-mid: #f6c5dc;
    --pink-deep: #ee9cc6;
    --white: #ffffff;
    --ink: #2a2a2a;
  }
  html, body { margin: 0; padding: 0; overflow: hidden; }
  body { width: 846px; height: 1200px; }
  .flyer {
    position: relative;
    width: 846px;
    height: 1200px;
    overflow: hidden;
    background:
      radial-gradient(ellipse at 70% 40%, var(--pink-light) 0%, var(--pink-mid) 60%, var(--pink-deep) 100%);
    font-family: "Roboto", Arial, sans-serif;
  }
  .model-photo {
    position: absolute;
    left: 0; top: 0;
    width: 430px; height: 1200px;
    background: linear-gradient(180deg, #f4e2cf 0%, #efd3bd 35%, #e9b6a6 55%, #ec94c2 75%, #e77fb6 100%);
    -webkit-mask-image: linear-gradient(90deg, #000 60%, transparent 100%);
    mask-image: linear-gradient(90deg, #000 60%, transparent 100%);
  }
  .brand {
    position: absolute;
    left: 262px; width: 545px; top: 30px;
    text-align: center;
  }
  .brand-name {
    font-family: "Baloo 2", sans-serif;
    font-weight: 800;
    font-size: 96px;
    line-height: 1;
    color: var(--red);
    margin: 0;
  }
  .brand-tag {
    font-family: "Roboto", sans-serif;
    font-size: 36px;
    letter-spacing: 25px;
    color: var(--ink);
    margin: 40px 0 0 25px;
    line-height: 1;
  }
  .intro {
    position: absolute;
    left: 300px; width: 490px; top: 258px;
    text-align: center;
    font-weight: 700;
    font-size: 22px;
    color: var(--red);
    margin: 0;
  }
  .headline {
    position: absolute;
    left: 300px; width: 496px; top: 292px;
    margin: 0;
    text-align: center;
    font-family: "Baloo 2", sans-serif;
    font-weight: 800;
    font-size: 104px;
    line-height: 94px;
    color: var(--white);
    -webkit-text-stroke: 9px var(--red);
    paint-order: stroke fill;
    text-shadow: 5px 6px 0 var(--red);
    letter-spacing: 1px;
  }
  .discount {
    position: absolute;
    left: 225px; top: 610px;
    width: 600px; height: 180px;
    color: var(--magenta);
    font-family: "Baloo 2", sans-serif;
    font-weight: 800;
  }
  .discount-upto {
    position: absolute;
    left: 8px; top: 36px;
    font-size: 36px;
    line-height: 34px;
    color: var(--red);
    -webkit-text-stroke: 6px var(--white);
    paint-order: stroke fill;
    text-align: center;
  }
  .discount-value {
    position: absolute;
    left: 70px; top: -20px;
    font-size: 210px;
    line-height: 1;
    -webkit-text-stroke: 10px var(--white);
    paint-order: stroke fill;
    letter-spacing: -4px;
  }
  .discount-percent {
    position: absolute;
    left: 322px; top: -8px;
    font-size: 100px;
    line-height: 1;
    -webkit-text-stroke: 8px var(--white);
    paint-order: stroke fill;
  }
  .discount-off {
    position: absolute;
    left: 312px; top: 62px;
    font-size: 108px;
    line-height: 1;
    -webkit-text-stroke: 8px var(--white);
    paint-order: stroke fill;
  }
  .sale-title {
    position: absolute;
    left: 300px; width: 490px; top: 782px;
    margin: 0;
    text-align: center;
    font-family: "Oswald", sans-serif;
    font-weight: 700;
    font-size: 80px;
    line-height: 1.1;
    color: var(--red);
    -webkit-text-stroke: 8px var(--white);
    paint-order: stroke fill;
  }
  .contact {
    position: absolute;
    left: 40px; top: 905px;
    color: var(--ink);
    font-size: 26px;
    line-height: 34px;
  }
  .contact p { margin: 0; }
  .contact strong { font-weight: 700; }
  .hours { margin-top: 26px !important; font-size: 20px; line-height: 29px; }
  .hours strong { display: block; }
  .map {
    position: absolute;
    left: 538px; top: 922px;
    width: 298px; height: 232px;
    background: linear-gradient(160deg, #fbeef4 0%, #f3d3e3 100%);
  }
  .map-caption {
    position: absolute;
    left: 538px; top: 1158px;
    margin: 0;
    font-family: "Tinos", serif;
    font-size: 14px;
    color: var(--ink);
  }
</style>
</head>
<body>
<main class="flyer">
  <div class="model-photo" role="img" aria-label="Photograph of a blonde woman in a pink lingerie top, seen from the shoulder"></div>

  <header class="brand">
    <h1 class="brand-name">Lunelle</h1>
    <p class="brand-tag">Lingerie</p>
  </header>

  <p class="intro">we want to let neighborhood know that</p>
  <h2 class="headline">WE OPEN<br>A NEW<br>STORE</h2>

  <div class="discount">
    <span class="discount-upto">UP<br>TO</span>
    <span class="discount-value">30</span>
    <span class="discount-percent">%</span>
    <span class="discount-off">OFF</span>
  </div>

  <h2 class="sale-title">Christmas Sale</h2>

  <section class="contact">
    <p><strong>Address:</strong></p>
    <p>shop 5/214 Marlow Crest Rd,<br>NSW 2173</p>
    <p><strong>Phone:</strong> 02 8415 3907</p>
    <p class="hours"><strong>Open hour:</strong>Mon - Fri 10:00am - 5:30pm<br>Sat - Sun 10:00am - 5:30pm</p>
  </section>

  <div class="map" role="img" aria-label="Street map showing the store location on Marlow Crest Rd"></div>
  <p class="map-caption">shop 5/214 Marlow Crest Rd, NSW 2173</p>
</main>
</body>
</html>
```